Need a FLYER/BROCHURE for selling woman hair. I have an online business and need your help.

I need a flyer/BROCHURE that represents my company. We sale hair online and needing for our customers to know our prices and discounts for any holiday and upcoming new year specials. I need the brochure to stand out. Have our brand Logo on it. Pictures of hair we sale on our site and models on the flyer. Prices will need to be place on the flyer indicating before and after the discounts. I also have a bag gift for loyal customers that need to be on the flyer. Colors I am interested in are purple and Gold. Or something creative that will blend with my logo. On my prices I sent. I need to change the title Best, Medium and Low Quality to 6A, 5A, to The Orlena Selection.

Reason: I would like the deadline to change. The reason I see some designers are coming to my project and some are saying the deadline is too short. I would like to see what they can offer me before I decide.

Industry/Entity Type

Business

Requirements
Must have
• Pictures of my brand. Prices that matches my original prices and sales prices. Pictures of hair and models.

```html
<!DOCTYPE html>
<html lang="en">
<head>
<meta charset="utf-8">
<title>Orlena Natural Hair – 2017 Price List</title>
<link rel="stylesheet" href="https://fonts.googleapis.com/css2?family=Cinzel:wght@700&family=Comfortaa:wght@700&family=Quicksand:wght@400&display=swap">
<style>
  :root {
    --paper: #f4f3f5;
    --band: #e9e7ea;
    --pink: #e05aa6;
    --pink-deep: #d0408f;
    --pink-soft: #e873b4;
    --gold-light: #ffe27a;
    --gold: #d9a52a;
    --gold-dark: #9c6a12;
    --white: #ffffff;
  }
  * { margin: 0; padding: 0; box-sizing: border-box; }
  html, body { width: 855px; height: 1200px; overflow: hidden; background: var(--paper); }
  .flyer { position: relative; width: 855px; height: 1200px; overflow: hidden; background: var(--paper); }
  .flyer__shapes { position: absolute; inset: 0; width: 855px; height: 1200px; }

  .gold-text {
    background: linear-gradient(180deg, var(--gold-light) 0%, var(--gold) 55%, var(--gold-dark) 100%);
    -webkit-background-clip: text;
    background-clip: text;
    color: transparent;
    filter: drop-shadow(2px 3px 2px rgba(60, 30, 20, 0.45));
  }

  .title {
    position: absolute; left: 44px; top: 228px;
    font-family: "Cinzel", "Times New Roman", serif;
    font-weight: 700; font-size: 66px; line-height: 66px;
    letter-spacing: 1px;
  }
  .title span { display: block; }

  .offer {
    position: absolute;
    font-family: "Comfortaa", "Arial Rounded MT Bold", sans-serif;
    font-weight: 700;
  }
  .offer--discounts { left: 206px; top: 590px; font-size: 46px; line-height: 70px; letter-spacing: 5px; }
  .offer--gift { left: 470px; top: 782px; text-align: center; }
  .offer--gift .offer__main { display: block; font-size: 46px; line-height: 56px; letter-spacing: 7px; margin-left: 24px; }
  .offer--gift .offer__sub { display: block; font-size: 25px; line-height: 32px; letter-spacing: 3px; }

  .brand {
    position: absolute; left: 490px; top: 520px; width: 260px;
    text-align: center;
    font-family: "Cinzel", "Times New Roman", serif;
    font-weight: 700; color: var(--gold);
    font-size: 40px; line-height: 44px;
  }

  .contact {
    position: absolute; left: 190px; top: 860px;
    font-family: "Quicksand", "Helvetica", sans-serif;
    font-weight: 400; color: var(--white);
    font-size: 20px; line-height: 29px; letter-spacing: 1px;
    font-style: normal;
  }
</style>
</head>
<body>
<main class="flyer">
  <svg class="flyer__shapes" viewBox="0 0 792 1111" preserveAspectRatio="none" aria-hidden="false">
    <defs>
      <linearGradient id="model-tone" x1="0" y1="0" x2="0.6" y2="1">
        <stop offset="0" stop-color="#d9b7a8"/>
        <stop offset="0.25" stop-color="#4a4c5a"/>
        <stop offset="0.7" stop-color="#1d2431"/>
        <stop offset="1" stop-color="#2c3340"/>
      </linearGradient>
      <linearGradient id="hair-tone" x1="0" y1="0" x2="1" y2="1">
        <stop offset="0" stop-color="#c98634"/>
        <stop offset="0.5" stop-color="#a9641b"/>
        <stop offset="1" stop-color="#e0a24c"/>
      </linearGradient>
    </defs>

    <path class="band" fill="var(--band)" d="M190,0 L360,0 C320,160 300,320 330,470 C360,620 480,660 560,700 C460,720 380,700 330,640 C250,540 250,380 230,260 C215,160 200,80 190,0 Z"/>

    <path class="blob blob--left" fill="var(--pink)" d="M0,0 L150,0 C70,50 160,120 220,200 C290,300 240,420 225,520 C205,650 140,760 150,900 C160,1000 250,1060 290,1111 L0,1111 Z"/>
    <path class="blob blob--left-edge" fill="var(--pink-soft)" d="M0,560 C40,590 70,640 60,720 C50,820 40,900 70,1000 C85,1060 110,1090 130,1111 L0,1111 Z"/>
    <path class="blob blob--corner" fill="var(--pink)" d="M0,0 L60,0 C40,40 20,70 0,80 Z"/>

    <path class="blob blob--photo-frame" fill="var(--pink)" d="M330,0 L792,0 L792,700 C700,690 610,650 530,630 C430,605 345,540 335,430 C322,300 325,150 330,0 Z"/>
    <path class="photo photo--model" role="img" aria-label="Photograph of a model with long, straight black hair" fill="url(#model-tone)" d="M345,210 C345,130 390,90 460,78 C530,66 560,20 600,0 L792,0 L792,645 C700,635 620,605 550,588 C450,565 352,505 345,400 Z"/>
    <path class="blob blob--photo-top" fill="var(--pink)" d="M370,0 L520,0 C500,35 460,55 420,50 C385,45 370,25 370,0 Z"/>

    <path class="blob blob--bottom" fill="var(--pink)" d="M240,1111 C290,1000 410,885 560,880 C680,876 740,878 792,858 L792,1111 Z"/>
    <path class="photo photo--hair" role="img" aria-label="Close-up photograph of wavy honey-blonde hair" fill="url(#hair-tone)" d="M110,1111 C190,1010 340,965 500,955 C620,948 720,960 792,935 L792,1111 Z"/>

    <path class="blob blob--contact" fill="var(--pink-deep)" d="M200,718 C262,690 320,728 332,760 C350,800 400,802 425,842 C442,882 382,922 322,942 C252,962 170,952 150,902 C134,852 160,740 200,718 Z"/>
  </svg>

  <h1 class="title gold-text"><span>2017</span><span>Price</span><span>List</span></h1>

  <div class="brand">Orlena<br>Natural Hair</div>

  <p class="offer offer--discounts gold-text">great<br>discounts</p>

  <p class="offer offer--gift gold-text">
    <span class="offer__main">a bag gift</span>
    <span class="offer__sub">for loyal customers</span>
  </p>

  <address class="contact">
    2450 Maple Lane<br>
    Fairdale, NY 11990<br>
    tel. 0155 555 0199<br>
    www.orlenahair.example
  </address>
</main>
</body>
</html>
```